Website redesign for a technology and engineering company

We'd like to redesign our website which can be found on quorvane.co.nz
!! Please find the designers brief as an uploaded file with all details in there!!
The main purpose for redesign is:
>change of services offered
>old website not very user friendly to maintain or update
Key requirements:
>visually appealing
>easy to navigate
>simple and easy to read
>responsive
>mobile device compatibility
>integrating best SEO practice
All the details are in the attached designer brief document.

```html
<!DOCTYPE html>
<html lang="en">
<head>
<meta charset="utf-8">
<title>Quorvane — Precision. Efficiency. Clarity</title>
<link href="https://fonts.googleapis.com/css2?family=Audiowide&family=Poppins:wght@400;500;600&display=swap" rel="stylesheet">
<style>
:root{
  --blue:#4479f5;
  --blue-dark:#3d6de0;
  --white:#ffffff;
  --grey:#f3f3f3;
  --ink:#111111;
  --black:#050505;
  --faint:rgba(0,0,0,0.035);
}
*{margin:0;padding:0;box-sizing:border-box}
html,body{width:1200px;height:4559px;overflow:hidden}
body{font-family:"Poppins",sans-serif;color:var(--ink);background:var(--white);position:relative}
.display{font-family:"Audiowide",sans-serif;text-transform:uppercase}

/* header */
.site-header{position:absolute;left:0;top:0;width:1200px;height:113px;background:var(--blue-dark)}
.logo{position:absolute;left:124px;top:32px;color:var(--white);font-size:34px;font-weight:500;letter-spacing:1px}
.logo-dot{display:inline-block;width:14px;height:14px;border-radius:50%;background:var(--white);margin-right:8px;vertical-align:middle}
.main-nav{position:absolute;left:440px;top:38px;display:flex;gap:10px;align-items:center}
.main-nav a{color:var(--white);text-decoration:none;font-size:14px;padding:3px 8px;border-radius:6px}
.main-nav a.active{border:1px solid var(--white)}
.socials{position:absolute;left:1025px;top:8px;display:flex;gap:5px}
.socials span{width:14px;height:14px;border-radius:50%;background:var(--white)}
.cta-top{position:absolute;left:942px;top:30px;width:156px;height:42px;border:2px solid var(--white);border-radius:6px;color:var(--white);font-size:14px;font-weight:600;display:flex;align-items:center;justify-content:center;gap:10px;background:var(--blue)}

/* hero */
.hero{position:absolute;left:0;top:113px;width:1200px;height:703px;background:var(--blue)}
.hero-ghost{position:absolute;left:0;width:1200px;top:40px;text-align:center;font-size:48px;color:rgba(255,255,255,0.07)}
.hero-title{position:absolute;left:0;width:1200px;top:75px;text-align:center;font-size:44px;color:var(--white);letter-spacing:2px}
.hero-btn{position:absolute;left:481px;top:161px;width:237px;height:53px;padding:0 14px;font-size:22px;background:var(--white);color:var(--blue);font-weight:500;display:flex;align-items:center;justify-content:space-between}
.hero-photo{position:absolute;left:175px;top:260px;width:850px;height:443px;background:linear-gradient(160deg,#6f8a5a 0%,#3f5a34 45%,#7b7d7a 75%,#5b5f58 100%)}
.slider-dots{position:absolute;left:566px;top:663px;display:flex;gap:6px}
.slider-dots span{width:16px;height:16px;border-radius:50%;border:2px solid var(--white)}
.slider-dots span.on{background:var(--white)}
.hero-arrow{position:absolute;top:255px}

/* shared */
.ghost{position:absolute;left:0;width:1200px;text-align:center;color:var(--faint);white-space:nowrap}
.section-title{position:absolute;left:0;width:1200px;text-align:center;font-size:44px;color:var(--ink);letter-spacing:2px}
.btn-small{position:absolute;height:30px;background:var(--white);color:var(--blue);font-size:11px;font-weight:600;display:flex;align-items:center;justify-content:space-between;padding:0 10px}

/* services */
.services{position:absolute;left:0;top:816px;width:1200px;height:1110px;background:var(--grey)}
.service-card{position:absolute;top:458px;width:321px;height:577px;background:var(--blue);color:var(--white)}
.service-badge{position:absolute;left:43px;top:-151px;width:235px;height:235px;transform:rotate(45deg);background:var(--blue);border-radius:26px;box-shadow:inset 0 0 0 6px rgba(255,255,255,0.25)}
.service-img{position:absolute;left:31px;top:-163px;width:260px;height:260px;border-radius:50%;transform:scale(.82)}
.service-card h3{position:absolute;left:15px;top:180px;font-size:28px;line-height:42px;font-weight:400}
.service-card ul{position:absolute;left:15px;top:278px;list-style:none;font-size:13px;line-height:21.8px}
.service-card li::before{content:"";display:inline-block;border-left:7px solid var(--white);border-top:5px solid transparent;border-bottom:5px solid transparent;margin-right:9px}
.service-card .btn-small{left:18px;top:513px;width:131px}

/* case studies */
.cases{position:absolute;left:0;top:1926px;width:1200px;height:764px;background:var(--white)}
.case-card{position:absolute;top:255px;width:239px;height:368px;background:var(--blue);color:var(--white);text-align:center}
.case-img{height:173px;width:100%}
.case-card h4{font-family:"Audiowide",sans-serif;font-weight:400;text-transform:uppercase;font-size:11px;line-height:17px;margin:16px 8px 8px}
.case-card p{font-size:9.5px;line-height:17px;margin:0 14px}
.case-card .btn-small{left:53px;top:325px;width:131px}
.case-arrows{position:absolute;left:563px;top:2590px;display:flex;gap:4px}

/* about */
.about{position:absolute;left:0;top:2690px;width:1200px;height:696px;background:linear-gradient(#f5f5f5 0,#f5f5f5 300px,#e9ecef 340px)}
.about-text{position:absolute;left:0;width:1200px;top:235px;text-align:center;font-size:11px;line-height:24px;color:#222}
.about-btn{position:absolute;left:534px;top:309px;width:131px;height:30px;background:var(--blue);color:var(--white);font-size:11px;font-weight:600;display:flex;align-items:center;justify-content:space-between;padding:0 10px}
.about-scene{position:absolute;left:0;top:330px;width:1200px;height:366px;background:linear-gradient(180deg,#e9ecef 0%,#b9c6b2 30%,#6f9a45 55%,#4f7d2c 100%)}

/* contact */
.contact{position:absolute;left:0;top:3386px;width:1200px;height:809px;background:var(--white)}
.contact-illustration{position:absolute;left:87px;top:242px;width:524px;height:322px;background:linear-gradient(180deg,#dbe6ff,#9db8f7);border-radius:12px}
.contact-line{position:absolute;left:96px;display:flex;align-items:center;gap:16px;font-size:17px;font-weight:500}
.contact-form{position:absolute;left:674px;top:242px;width:438px;height:468px;background:var(--blue)}
.field{position:absolute;left:18px;width:404px;background:var(--white);font-size:14px;padding:10px 18px;color:#333}
.send{position:absolute;left:18px;top:388px;width:156px;height:46px;background:var(--white);font-size:15px;font-weight:500;display:flex;align-items:center;justify-content:center}

/* footer */
.site-footer{position:absolute;left:0;top:4195px;width:1200px;height:315px;background:var(--black);color:var(--white)}
.footer-logo{position:absolute;left:90px;top:72px;font-size:34px;font-weight:500}
.footer-about{position:absolute;left:90px;top:164px;font-size:12px;line-height:23px;width:260px}
.footer-col{position:absolute;top:100px}
.footer-col h5{font-family:"Audiowide",sans-serif;font-weight:400;font-size:15px;text-transform:lowercase;letter-spacing:1px;margin-bottom:24px}
.footer-col a{display:block;color:var(--white);text-decoration:none;font-size:12px;margin-bottom:24px}
.footer-col a::before{content:"↗ ";color:var(--blue)}
.footer-social{display:flex;gap:8px}
.footer-social span{width:24px;height:24px;border-radius:50%;background:var(--blue)}
.subscribe{display:flex;margin-top:30px}
.subscribe span:first-child{width:114px;height:27px;background:var(--white);color:#444;font-size:8px;display:flex;align-items:center;padding-left:8px}
.subscribe span:last-child{width:62px;height:27px;background:var(--blue);font-size:8px;display:flex;align-items:center;justify-content:center}
.copyright{position:absolute;left:0;top:4510px;width:1200px;height:49px;background:var(--blue);color:var(--white);font-family:"Audiowide",sans-serif;font-size:11px;letter-spacing:2px;display:flex;align-items:center;justify-content:center}
</style>
</head>
<body>

<header class="site-header">
  <div class="logo"><span class="logo-dot"></span>Quorvane</div>
  <nav class="main-nav">
    <a href="#">HOME</a>
    <a href="#" class="active">SERVICES OFFERED</a>
    <a href="#">CASE STUDY</a>
    <a href="#">ABOUT</a>
    <a href="#">CONTACT</a>
  </nav>
  <div class="socials"><span></span><span></span><span></span></div>
  <div class="cta-top">GET IN TOUCH
    <svg width="16" height="16" viewBox="0 0 16 16"><path d="M2 14L14 2M5 2h9v9" stroke="#fff" stroke-width="1.8" fill="none"/></svg>
  </div>
</header>

<section class="hero">
  <div class="hero-ghost display">Precision. Efficiency. Clarity</div>
  <h1 class="hero-title display">Precision. Efficiency. Clarity</h1>
  <div class="hero-btn">LEARN MORE
    <svg width="24" height="24" viewBox="0 0 24 24"><path d="M3 21L21 3M7 3h14v14" stroke="#4479f5" stroke-width="2.2" fill="none"/></svg>
  </div>
  <svg class="hero-arrow" style="left:86px" width="46" height="80" viewBox="0 0 46 80"><path d="M44 2A38 38 0 0 0 44 78" stroke="#fff" stroke-width="3" fill="none"/><path d="M32 30L22 40L32 50" stroke="#fff" stroke-width="3" fill="none"/></svg>
  <svg class="hero-arrow" style="left:1068px" width="46" height="80" viewBox="0 0 46 80"><path d="M2 2A38 38 0 0 1 2 78" stroke="#fff" stroke-width="3" fill="none"/><path d="M14 30L24 40L14 50" stroke="#fff" stroke-width="3" fill="none"/></svg>
  <div class="hero-photo" role="img" aria-label="Field technician beside a solar-powered GNSS monitoring station on a roadside"></div>
  <div class="slider-dots"><span class="on"></span><span></span><span></span></div>
</section>

<section class="services">
  <div class="ghost display" style="top:70px;font-size:150px">Services</div>
  <h2 class="section-title display" style="top:180px">Services</h2>

  <article class="service-card" style="left:90px">
    <div class="service-badge"></div>
    <div class="service-img" style="background:linear-gradient(180deg,#9cc3e8,#4d6f86 55%,#c53a3a)" role="img" aria-label="Boat on the water approaching a rocky island"></div>
    <h3 class="display">Fieldwork<br>Solutions</h3>
    <ul>
      <li>Project management &amp; logistics</li>
      <li>Efficient product rollouts</li>
      <li>Equipment Installation &amp; Maintenance</li>
      <li>Surveying Techniques</li>
      <li>Precision GNSS instrumentation</li>
      <li>Seismic Instrumentation</li>
      <li>IOT Sensors</li>
      <li>Reliable Communications Systems</li>
      <li>Environmental sensors</li>
    </ul>
    <div class="btn-small">READ MORE <svg width="14" height="14" viewBox="0 0 14 14"><path d="M2 12L12 2M4 2h8v8" stroke="#4479f5" stroke-width="1.6" fill="none"/></svg></div>
  </article>

  <article class="service-card" style="left:440px">
    <div class="service-badge"></div>
    <div class="service-img" style="background:linear-gradient(180deg,#c9d4dc,#8fa0a8 50%,#7a6a45)" role="img" aria-label="Monitoring station on a coastal hilltop"></div>
    <h3 class="display">Positioning and<br>Monitoring</h3>
    <ul>
      <li>Real-Time Kinematic (RTK) Solutions</li>
      <li>Custom GNSS Base stations</li>
      <li>NTRIP service</li>
      <li>Tailored Monitoring Solutions</li>
      <li>Environmental Monitoring</li>
      <li>Robust communication Systems</li>
      <li>Internet of Things (IoT) Integration</li>
      <li>Solar powered systems</li>
      <li>Smart Sensor Networks</li>
    </ul>
    <div class="btn-small">READ MORE <svg width="14" height="14" viewBox="0 0 14 14"><path d="M2 12L12 2M4 2h8v8" stroke="#4479f5" stroke-width="1.6" fill="none"/></svg></div>
  </article>

  <article class="service-card" style="left:790px">
    <div class="service-badge"></div>
    <div class="service-img" style="background:linear-gradient(160deg,#e6e8ea,#b9bdc1)" role="img" aria-label="Machined mechanical parts and callipers on technical drawings"></div>
    <h3 class="display">Design and<br>Prototyping</h3>
    <ul>
      <li>Mechanical Component Design</li>
      <li>Robust Field Equipment Infrastructure</li>
      <li>Remote Monitoring System Design</li>
      <li>3D modelling</li>
      <li>Standalone Power Solutions</li>
      <li>Wireless Communication Solutions</li>
      <li>Real-Time Data Transmission</li>
      <li>Rapid Prototyping</li>
      <li>Field Deployment and Testing</li>
    </ul>
    <div class="btn-small">READ MORE <svg width="14" height="14" viewBox="0 0 14 14"><path d="M2 12L12 2M4 2h8v8" stroke="#4479f5" stroke-width="1.6" fill="none"/></svg></div>
  </article>
</section>

<section class="cases">
  <div class="ghost display" style="top:90px;font-size:100px">Case Studies</div>
  <h2 class="section-title display" style="top:152px">Case Studies</h2>

  <article class="case-card" style="left:87px">
    <div class="case-img" style="background:linear-gradient(180deg,#7f9482,#8b8a7c)" role="img" aria-label="Remote camera mast on a rocky alpine ridge"></div>
    <h4>Remote Camera Installation<br>in Alpine Environment</h4>
    <p>Successful installation of advanced camera systems in the challenging and remote alpine regions of Fiordland.</p>
    <div class="btn-small">READ MORE <svg width="14" height="14" viewBox="0 0 14 14"><path d="M2 12L12 2M4 2h8v8" stroke="#4479f5" stroke-width="1.6" fill="none"/></svg></div>
  </article>

  <article class="case-card" style="left:350px">
    <div class="case-img" style="background:linear-gradient(180deg,#3d7ad1,#9fb5c9 50%,#6b6a5f)" role="img" aria-label="GNSS station on a mountain summit"></div>
    <h4>GNSS CORS Station Upgrade<br>and Survey</h4>
    <p>Upgrade and reference mark survey of GNSS Continuously Operating Reference Stations (CORS) for the Veltaro positioning network.</p>
    <div class="btn-small">READ MORE <svg width="14" height="14" viewBox="0 0 14 14"><path d="M2 12L12 2M4 2h8v8" stroke="#4479f5" stroke-width="1.6" fill="none"/></svg></div>
  </article>

  <article class="case-card" style="left:612px">
    <div class="case-img" style="background:linear-gradient(180deg,#3f7fe0,#8fb7ee)" role="img" aria-label="Communications tower with satellite dishes"></div>
    <h4>Communications<br>Hub Upgrade</h4>
    <p>Installation of a satellite interface for Terravon to ensure reliable data transmission for scientific research and monitoring of geological hazards.</p>
    <div class="btn-small">READ MORE <svg width="14" height="14" viewBox="0 0 14 14"><path d="M2 12L12 2M4 2h8v8" stroke="#4479f5" stroke-width="1.6" fill="none"/></svg></div>
  </article>

  <article class="case-card" style="left:876px">
    <div class="case-img" style="background:linear-gradient(90deg,#7d8a5a,#a9a48a 50%,#6f7d4e)" role="img" aria-label="Aerial view of a damaged railway line in a river valley"></div>
    <h4>Aerial Survey for Post-Di-<br>saster Recovery</h4>
    <p>Survey to assess damage to the railway line caused by Cyclone Marelo and create a digital terrain model (DTM) and orthophoto for engineers to plan and rebuild.</p>
    <div class="btn-small">READ MORE <svg width="14" height="14" viewBox="0 0 14 14"><path d="M2 12L12 2M4 2h8v8" stroke="#4479f5" stroke-width="1.6" fill="none"/></svg></div>
  </article>
</section>
<div class="case-arrows">
  <svg width="34" height="48" viewBox="0 0 34 48"><path d="M32 2A22 22 0 0 0 32 46" stroke="#4479f5" stroke-width="3" fill="none"/><path d="M24 17L17 24L24 31" stroke="#4479f5" stroke-width="2" fill="none"/></svg>
  <svg width="34" height="48" viewBox="0 0 34 48"><path d="M2 2A22 22 0 0 1 2 46" stroke="#4479f5" stroke-width="3" fill="none"/><path d="M10 17L17 24L10 31" stroke="#4479f5" stroke-width="2" fill="none"/></svg>
</div>

<section class="about">
  <div class="about-scene" role="img" aria-label="Grassy hillside with a solar-powered monitoring station and a utility vehicle under misty sky"></div>
  <div class="ghost display" style="top:100px;font-size:100px">About</div>
  <h2 class="section-title display" style="top:155px">About</h2>
  <p class="about-text">Welcome to Quorvane, your reliable partner in delivering innovative solutions. Our team of skilled professionals<br>is committed to excellence, ensuring every project is handled with precision, efficiency, and integrity.</p>
  <div class="about-btn">READ MORE <svg width="14" height="14" viewBox="0 0 14 14"><path d="M2 12L12 2M4 2h8v8" stroke="#fff" stroke-width="1.6" fill="none"/></svg></div>
</section>

<section class="contact">
  <div class="ghost display" style="top:95px;font-size:70px">Get in touch with us!</div>
  <h2 class="section-title display" style="top:130px">Get in touch with us!</h2>
  <div class="contact-illustration" role="img" aria-label="Illustration of a support agent with headset working at a laptop beside speech bubbles"></div>

  <div class="contact-line" style="top:587px">
    <svg width="42" height="42" viewBox="0 0 42 42"><circle cx="21" cy="21" r="21" fill="#4479f5"/><path d="M14 11c2 0 3 4 3 5s-2 2-2 3c1 3 4 6 7 7 1 0 2-2 3-2s5 1 5 3-2 4-4 4C18 31 11 24 11 14c0-2 2-3 3-3z" fill="#fff"/></svg>
    XX XXXX XX
  </div>
  <div class="contact-line" style="top:649px">
    <svg width="42" height="42" viewBox="0 0 42 42"><circle cx="21" cy="21" r="21" fill="#4479f5"/><rect x="10" y="13" width="22" height="16" rx="2" fill="none" stroke="#fff" stroke-width="2"/><path d="M10 14l11 9 11-9" fill="none" stroke="#fff" stroke-width="2"/></svg>
    hi@quorvane.nz
  </div>

  <form class="contact-form">
    <div class="field" style="top:44px;height:45px">Name</div>
    <div class="field" style="top:103px;height:46px">Email</div>
    <div class="field" style="top:165px;height:44px">Subject</div>
    <div class="field" style="top:225px;height:140px">Message(Optional)</div>
    <div class="send">Send</div>
  </form>
</section>

<footer class="site-footer">
  <div class="footer-logo">Quorvane</div>
  <p class="footer-about">We are field operations experts with backgrounds in surveying, geoscience, and technical field work.</p>
  <div class="footer-col" style="left:460px">
    <h5>Main Menu</h5>
    <a href="#">Home</a>
    <a href="#">About</a>
  </div>
  <div class="footer-col" style="left:694px">
    <h5>Quick Links</h5>
    <a href="#">Services</a>
    <a href="#">Case Study</a>
  </div>
  <div class="footer-col" style="left:937px">
    <h5>Get in Touch</h5>
    <div class="footer-social"><span></span><span></span><span></span></div>
    <div class="subscribe"><span>Enter your email here</span><span>Subscribe</span></div>
  </div>
</footer>
<div class="copyright">Copyright © Quorvane 2024. All Rights Reserved.</div>

</body>
</html>
```